Winsome Luxury Flower Shop

Need a beautiful, eye catching, elegant full-service website.
INSPIRATIONS ARE;
https://www.quillmarshblooms.com

Industry/Entity Type

retail, floral, boutique

Coding

Coded - Design and coding required

Number of Pages Required

3 page

Requirements
Must have
• SEO, Coded, UX, Fully responsive mobile, tablet, desktop, Ecommerce setup with Square, payments integration (if we use squarespace). SEO optimization with keywords, tags, meta descriptions, Load speed optimization, Google my business setup.
Nice to have
• pictures, color, elegance

```html
<!DOCTYPE html>
<html lang="en">
<head>
<meta charset="utf-8">
<title>Winsome Flower Boutique</title>
<link href="https://fonts.googleapis.com/css2?family=Libre+Baskerville:wght@400;700&family=Lora:ital,wght@0,400;1,400&family=Roboto:wght@400;500&display=swap" rel="stylesheet">
<style>
:root{
  --red:#c8202a;
  --red-dark:#a8161e;
  --black:#0b0b0b;
  --ink:#222;
  --muted:#666;
  --grey-bg:#ececec;
  --white:#fff;
}
*{box-sizing:border-box;margin:0;padding:0}
html,body{width:1200px;height:4514px;overflow:hidden}
body{position:relative;background:var(--white);font-family:"Roboto",Arial,sans-serif;color:var(--ink)}
.abs{position:absolute}
.italic{font-family:"Lora",Georgia,serif;font-style:italic}

/* top bar */
.topbar{left:0;top:0;width:1200px;height:38px;background:var(--red);color:#fff;font-size:13px}
.topbar .call{left:112px;top:11px}
.topbar .promo{left:0;width:1200px;text-align:center;top:11px}
.topbar .promo u{color:#f3c1c4}
.topbar .social{right:112px;top:12px;display:flex;gap:10px}
.topbar .social span{width:12px;height:12px;border:1.5px solid #fff;border-radius:50%}

/* header */
.header{left:0;top:38px;width:1200px;height:97px;background:#fff}
.header-bar{left:425px;top:40px;display:flex;align-items:flex-start;gap:18px}
.nav{display:flex;gap:20px;font-size:11px;font-family:"Libre Baskerville",Georgia,serif;color:#222;white-space:nowrap}
.nav .active{color:var(--red);text-align:center}
.nav .active::after{content:"";display:block;width:10px;height:10px;border-radius:50%;background:var(--red);margin:8px auto 0}
.icons{display:flex;gap:22px;margin-top:-3px}
.logo{left:114px;top:44px;width:180px;height:132px;border-radius:50%;background:#fff;z-index:5;display:flex;align-items:center;justify-content:center;box-shadow:0 2px 6px rgba(0,0,0,.15)}
.logo span{font-family:"Libre Baskerville",Georgia,serif;font-size:26px;font-weight:700;color:var(--black)}

/* hero */
.hero{left:0;top:135px;width:1200px;height:650px;background:linear-gradient(120deg,#5a3a2c 0%,#8e5a45 40%,#c98d86 70%,#6b4a3a 100%)}
.hero-panel{left:91px;top:198px;width:596px;height:277px;background:rgba(200,32,42,.82);border-radius:6px;color:#fff;padding:30px 24px 0;display:flex;flex-direction:column;align-items:flex-start}
.hero-panel h1{font-family:"Libre Baskerville",Georgia,serif;font-size:29px;line-height:42px;font-weight:700;white-space:nowrap}
.hero-panel p{margin-top:16px;width:548px;font-size:14px;line-height:24px}
.btn-dark{background:var(--black);color:#fff;border-radius:24px;font-family:"Libre Baskerville",Georgia,serif;font-size:14px;font-weight:700;display:flex;align-items:center;justify-content:center}
.hero-panel .btn-dark{margin-top:16px;width:147px;height:46px;flex:none}
.dots{left:574px;top:623px;display:flex;gap:6px}
.dots span{width:11px;height:11px;border-radius:50%;border:1.5px solid #fff}
.dots span:first-child{background:var(--red);border-color:var(--red)}

/* section titles */
.title-line{left:0;width:1200px;text-align:center}
.title-line h2{display:inline-block;font-family:"Libre Baskerville",Georgia,serif;font-weight:400;font-size:29px;padding:8px 22px;border-top:1px solid #999;border-bottom:1px solid #999;color:#222}

/* featured */
.tabs{left:180px;top:912px;width:845px;display:flex;justify-content:space-between;font-family:"Libre Baskerville",Georgia,serif;font-size:12px;color:#333;border-bottom:1px solid #ddd;padding:0 8px 14px}
.tabs .on{position:relative}
.tabs .on::after{content:"";position:absolute;left:-10px;right:-10px;bottom:-15px;height:3px;background:var(--red)}
.card{top:979px;width:314px;height:406px}
.card .photo{width:100%;height:100%}
.card .label{position:absolute;left:16px;right:16px;top:381px;height:47px;background:var(--black);color:#fff;font-family:"Libre Baskerville",Georgia,serif;font-size:17px;display:flex;align-items:center;justify-content:center}
.card .label.red{background:var(--red)}

/* about */
.about{left:0;top:1473px;width:1200px;height:480px;background:linear-gradient(100deg,#6b4d37 0%,#a27a5c 45%,#4d4036 100%)}
.about h2{position:absolute;left:771px;top:212px;color:#fff;font-family:"Libre Baskerville",Georgia,serif;font-size:30px;font-weight:700}
.about p{position:absolute;left:771px;top:262px;width:370px;color:#fff;font-size:13px;line-height:26px}
.btn-red{background:var(--red);color:#fff;border-radius:26px;font-family:"Libre Baskerville",Georgia,serif;font-size:14px;display:flex;align-items:center;justify-content:center;gap:10px}
.about .btn-red{position:absolute;left:771px;top:357px;width:180px;height:46px}

.signup{left:0;top:1953px;width:1200px;height:79px;background:var(--red);color:#fff;font-family:"Libre Baskerville",Georgia,serif;font-size:26px;font-weight:700;text-align:center;line-height:79px}
.signup em{font-style:normal;color:#2a0a0a}

/* feature rows */
.row{left:0;width:1200px;height:403px}
.row .photo{position:absolute;top:0;width:600px;height:403px}
.row .text{position:absolute;top:0;width:600px;height:403px}
.row h2{position:absolute;left:67px;top:85px;font-family:"Libre Baskerville",Georgia,serif;font-size:30px;font-weight:700;color:#222}
.row h2::after{content:"";display:block;width:52px;height:3px;background:var(--red);margin-top:10px}
.row p{position:absolute;left:67px;top:150px;width:400px;font-size:13px;line-height:26px;color:#555}
.row .btn-red{position:absolute;left:67px;top:305px;width:155px;height:46px}

/* testimonials */
.testi{left:0;top:3241px;width:1200px;height:564px;background:var(--grey-bg)}
.tcard{top:165px;width:303px;height:273px;background:#fff;box-shadow:0 2px 8px rgba(0,0,0,.08);padding:20px 18px}
.tcard .stars{color:#f0a020;font-size:14px;letter-spacing:2px}
.tcard h3{font-family:"Libre Baskerville",Georgia,serif;font-size:15px;font-weight:400;margin-top:8px}
.tcard .quote{position:absolute;right:18px;top:12px;font-family:"Libre Baskerville",Georgia,serif;font-size:110px;line-height:1;color:#eee}
.tcard p{font-family:"Lora",Georgia,serif;font-style:italic;font-size:12px;line-height:21.5px;color:#666;margin-top:22px;position:relative}
.testi .btn-red{position:absolute;left:508px;top:470px;width:186px;height:47px;font-size:13px}

/* newsletter */
.news{left:0;top:3805px;width:1200px;height:340px;background:linear-gradient(180deg,#c8202a,#b81c24)}
.news .title-line h2{color:#fff;border-color:#f1a4a8}
.news p{position:absolute;left:270px;top:153px;width:660px;text-align:center;color:#fff;font-family:"Lora",Georgia,serif;font-style:italic;font-size:14px;line-height:26px}
.news .field{position:absolute;left:258px;top:223px;width:685px;height:45px;background:#fff;border-radius:24px;font-family:"Lora",Georgia,serif;font-style:italic;font-size:13px;color:#555;padding:14px 18px}
.news .field .btn-dark{position:absolute;right:3px;top:3px;width:158px;height:39px;font-style:normal;font-family:"Roboto",Arial,sans-serif;font-weight:500;font-size:13px}

/* footer */
.footer{left:0;top:4145px;width:1200px;height:369px;background:var(--black);color:#fff}
.flogo{left:119px;top:60px;width:258px;height:166px;display:flex;align-items:center;justify-content:center;font-family:"Libre Baskerville",Georgia,serif;font-size:38px;font-weight:700}
.footer h4{position:absolute;top:46px;font-family:"Libre Baskerville",Georgia,serif;font-size:19px;font-weight:700}
.contact{left:401px;display:flex;gap:16px;font-size:13px;line-height:19px}
.contact .ic{width:40px;height:40px;border:1.5px solid #fff;border-radius:50%;display:flex;align-items:center;justify-content:center;flex:none}
.list{font-size:13.5px;line-height:30px}
.list li{list-style:none;padding-left:36px;position:relative;white-space:nowrap}
.list li::before{content:"›";position:absolute;left:2px;font-size:18px}
.fsocial{left:875px;top:220px;display:flex;gap:14px}
.fsocial span{width:40px;height:40px;border:1.5px solid #fff;border-radius:50%}
.fsocial span.on{background:var(--red);border-color:var(--red)}
.copy{left:112px;top:310px;width:976px;border-top:1px solid #333;text-align:center;padding-top:14px;font-size:13px}
</style>
</head>
<body>

<div class="abs topbar">
  <div class="abs call">Call Us : 000-000-00000</div>
  <div class="abs promo">Sign up and GET30% OFF for your first order <u>Sign up now</u></div>
  <div class="abs social"><span></span><span></span><span></span></div>
</div>

<div class="abs header">
  <div class="abs header-bar">
    <nav class="nav">
      <span class="active">HOME</span><span>ABOUT US</span><span>PRODUCTS</span><span>OCCASIONS</span><span>TESTIMONIALS</span><span>CONTACT US</span>
    </nav>
    <div class="icons">
      <svg width="18" height="18" viewBox="0 0 18 18" fill="none" stroke="#333" stroke-width="1.6"><circle cx="7.5" cy="7.5" r="5.5"/><path d="M11.5 11.5l5 5"/></svg>
      <svg width="18" height="18" viewBox="0 0 18 18" fill="none" stroke="#333" stroke-width="1.6"><circle cx="9" cy="6" r="3.5"/><path d="M2.5 17c0-4 3-6 6.5-6s6.5 2 6.5 6"/></svg>
      <svg width="18" height="18" viewBox="0 0 18 18" fill="none" stroke="#333" stroke-width="1.6"><path d="M3 5h12l-1 11H4z"/><path d="M6.5 7V4a2.5 2.5 0 0 1 5 0v3"/></svg>
    </div>
  </div>
</div>
<div class="abs logo"><span>WINSOME</span></div>

<section class="abs hero" role="img" aria-label="Wrapped rose bouquets in kraft paper on a wooden florist table">
  <div class="abs hero-panel">
    <h1>WELCOME TO<br>WINSOME FLOWER BOUTIQUE</h1>
    <p class="italic">The point of using Lorem Ipsum is that it has a more-or-less normal distribution of letters, as opposed to using 'Content here</p>
    <div class="btn-dark">SHOP NOW</div>
  </div>
  <div class="abs dots"><span></span><span></span><span></span></div>
</section>

<div class="abs title-line" style="top:830px"><h2>FEATURED PRODUCTS</h2></div>
<div class="abs tabs"><span class="on">ALL</span><span>ANNIVERSARY</span><span>BIRTHDAY</span><span>CONGRATULATIONS</span><span>HOUSEWARMING</span><span>SYMPATHY</span><span>THANK YOU</span></div>

<div class="abs card" style="left:112px">
  <div class="photo" role="img" aria-label="Anniversary bouquet with green chrysanthemums and roses" style="background:linear-gradient(160deg,#5f7a55,#b9a07a 60%,#e0b79a)"></div>
  <div class="label">ANNIVERSARY</div>
</div>
<div class="abs card" style="left:443px">
  <div class="photo" role="img" aria-label="Birthday card resting on pink peonies and roses" style="background:linear-gradient(160deg,#f3b9c4,#f4e8ea 50%,#ef9fb0)"></div>
  <div class="label red">BIRTHDAY</div>
</div>
<div class="abs card" style="left:774px">
  <div class="photo" role="img" aria-label="Pastel bridal bouquet held in hands" style="background:linear-gradient(160deg,#e8e4e0,#e9c4c4 55%,#d8d0c8)"></div>
  <div class="label">WEDDINGS</div>
</div>

<section class="abs about" role="img" aria-label="Florist hands wrapping a rose bouquet in kraft paper">
  <h2>ABOUT WINSOME</h2>
  <p class="italic">The point of using Lorem Ipsum is that it has a more-or-less normal distribution of letters, as opposed to using 'Content content heremaking it look like readable English.</p>
  <div class="btn-red">WATCH VIDEO
    <svg width="22" height="22" viewBox="0 0 22 22"><circle cx="11" cy="11" r="9.5" fill="none" stroke="#fff" stroke-width="1.6"/><path d="M9 7l6 4-6 4z" fill="#fff"/></svg>
  </div>
</section>

<div class="abs signup">Sign up and <em>GET30% OFF</em> for your first order <u>Sign up now</u></div>

<section class="abs row" style="top:2032px">
  <div class="photo" style="left:0;background:linear-gradient(120deg,#8a6d5a,#d7c2b2 50%,#e8a9a0)" role="img" aria-label="Florist arranging flowers in a wicker basket"></div>
  <div class="text" style="left:600px">
    <h2>POPULAR THIS WEEK</h2>
    <p>It is a long established fact that a reader will be distracted by the readable content of a page when looking at its layout. The point of using Lorem Ipsum is that it has a more-or-less normal distribution of letters, as opposed to using 'Content content here making it look like readable English.</p>
    <div class="btn-red">VIEW MORE</div>
  </div>
</section>

<section class="abs row" style="top:2435px">
  <div class="text" style="left:0">
    <h2 style="left:152px">SPECIAL OFFERS</h2>
    <p style="left:152px">It is a long established fact that a reader will be distracted by the readable content of a page when looking at its layout. The point of using Lorem Ipsum is that it has a more-or-less normal distribution of letters, as opposed to using 'Content content here making it look like readable English.</p>
    <div class="btn-red" style="left:156px">VIEW MORE</div>
  </div>
  <div class="photo" style="left:600px;background:linear-gradient(140deg,#b08a5c,#d8b98f 50%,#8f6a44)" role="img" aria-label="Florist tools, twine and fresh stems on a wooden table"></div>
</section>

<section class="abs row" style="top:2838px">
  <div class="photo" style="left:0;background:linear-gradient(120deg,#e9c9c9,#f2a7a6 50%,#e6b9ae)" role="img" aria-label="Pink gerberas and roses in a gift box"></div>
  <div class="text" style="left:600px">
    <h2>GIFTS &amp; FLOWER</h2>
    <p>It is a long established fact that a reader will be distracted by the readable content of a page when looking at its layout. The point of using Lorem Ipsum is that it has a more-or-less normal distribution of letters, as opposed to using 'Content content here making it look like readable English.</p>
    <div class="btn-red">VIEW MORE</div>
  </div>
</section>

<section class="abs testi">
  <div class="abs title-line" style="top:62px"><h2>WHAT OUR CLIENTS SAYING</h2></div>
  <div class="abs tcard" style="left:112px"><div class="quote">”</div><div class="stars">★★★★☆</div><h3>ALEX DEV</h3><p>It is a long established fact that a reader will be distracted by the readable content of page when looking at its layout. The point of using Lorem Ipsum is that it has a more-or-less normal distribution of letters the point of using Lorem Ipsum is that it has a more less normal distribution of letters</p></div>
  <div class="abs tcard" style="left:449px"><div class="quote">”</div><div class="stars">★★★★☆</div><h3>ALEX DEV</h3><p>It is a long established fact that a reader will be distracted by the readable content of page when looking at its layout. The point of using Lorem Ipsum is that it has a more-or-less normal distribution of letters the point of using Lorem Ipsum is that it has a more less normal distribution of letters</p></div>
  <div class="abs tcard" style="left:785px"><div class="quote">”</div><div class="stars">★★★★☆</div><h3>ALEX DEV</h3><p>It is a long established fact that a reader will be distracted by the readable content of page when looking at its layout. The point of using Lorem Ipsum is that it has a more-or-less normal distribution of letters the point of using Lorem Ipsum is that it has a more less normal distribution of letters</p></div>
  <div class="btn-red">VIEW MORE REVIEWS</div>
</section>

<section class="abs news">
  <div class="abs title-line" style="top:80px"><h2>OUR NEWSLETTER SIGNUP</h2></div>
  <p>Lorem ipsum dolor sit amet, consectetur adipiscing elit, sed do eiusmod tempor incididunt ut labore et enim ad minim veniam, quis nostrud exercitation ullamco</p>
  <div class="field">Enter Email Address :<div class="btn-dark">SUBSCRIBE</div></div>
</section>

<footer class="abs footer">
  <div class="abs flogo">WINSOME</div>
  <h4 style="left:401px">ADDRESS</h4>
  <h4 style="left:666px">QUICK LINKS</h4>
  <h4 style="left:874px">STORE HOURS</h4>

  <div class="abs contact" style="top:95px">
    <div class="ic"><svg width="18" height="18" viewBox="0 0 18 18"><path d="M4 2l3 3-2 2c1 2 3 4 5 5l2-2 3 3-2 3C7 16 2 11 1 5z" fill="#fff"/></svg></div>
    <div>PHONE NUMBER<br>000.000.0000</div>
  </div>
  <div class="abs contact" style="top:155px">
    <div class="ic"><svg width="18" height="14" viewBox="0 0 18 14"><rect x="1" y="1" width="16" height="12" fill="#fff"/><path d="M1 1l8 7 8-7" fill="none" stroke="#0b0b0b" stroke-width="1.4"/></svg></div>
    <div>EMAIL US<br>info@winsomeblooms.com</div>
  </div>
  <div class="abs contact" style="top:215px">
    <div class="ic"><svg width="14" height="20" viewBox="0 0 14 20"><path d="M7 1a6 6 0 0 1 6 6c0 5-6 12-6 12S1 12 1 7a6 6 0 0 1 6-6z" fill="#fff"/><circle cx="7" cy="7" r="2.3" fill="#0b0b0b"/></svg></div>
    <div>ADDRESS<br>2236 72nd Lorem ipsum<br>Duumy lorem</div>
  </div>

  <ul class="abs list" style="left:666px;top:90px">
    <li>Home</li><li>About Us</li><li>Products</li><li>Occasions</li><li>Testimonials</li><li>Gallery</li><li>Contact Us</li>
  </ul>
  <ul class="abs list" style="left:874px;top:90px">
    <li>Monday - Friday 9am - 4pm</li><li>Saturday - 10am - 4pm</li><li>Sunday - 11am - 4pm</li>
  </ul>
  <div class="abs fsocial"><span></span><span class="on"></span><span></span></div>
  <div class="abs copy">©2025 Winsome. All rights reserved.</div>
</footer>

</body>
</html>
```